Lantern Lane Town Footpath Chronicle Trek

We are launching a different kind of city historical walking tour company with a slightly darker approach using historical but real stories that have long been forgotten from living memory.
Our tour is going to contain a lot of very thoroughly researched stories ranging from 50 to 150 years past that takes the customer into the actual-real life past of the city streets.  Stories that may contains some dark undertones and stories with a twist or that seem eccentric to us now but were entirely normal back in olden times - minus the dry historical facts that most tours engage in..
Our tours are going to run both day and night and will incorporate real history / real Lantern Lane, so some of the stories will be quite serious (e.g.- there are actual murders from 100 years ago, baffling court cases, even a bit of poetry written by murderers, suicides, love triangles, you name it.  We are aiming for a mystery/history theme and are aiming to attract tourists who are interested in getting a different kind of history.

We're not going for scares and even though we expect people to enjoy our tours;  we're not aiming at light fun and frivolity.  I guess if you wanted to give us a tv rating we'd be aiming at M to MA15+.
If I was to give you another analogy using the literature world.  Think Edwin Harrowgates Nocturno rather than the Moonrise Saga of movies.  Or Clara Wendham's Gravemoor rather than the Pickwells.  Even Crown of Embers rather than a soap opera.
Our stories are being carefully crafted and are packed with unexpected twists, turns & revelations whilst remaining all 100% true.  We have approx 15-20 stories for each tour and we're designing them in a way that each story will trigger a different range of emotions in the listeners on a regular basis.  We're being very careful to keep it fresh for each story so that it will next to impossible for our guests to zone out!  I personally can't stand going on a tour where mildly interesting facts are read out.  We like deep, rich stories rather than pop entertainment.
We want the website to generate a feeling/atmosphere for our product that draws the right crowd to our tours as well as making it easy to make a booking.  Basic features to include:-
Home Page
Bookings Page
Integration with a booking system will be required here via use of plugin code.
Private Functions Page
We are hoping to integrate with a booking system via use of plugin code.  If not, then a simple form enquiry type input e.g.- name, emails, subject, contact, details, preferred date/time, etc).
About Us Page :-
Dark; a euphemism for the unknown or the forgotten.  Think dark ages, dark matter, dark energy; things where knowledge is uncertain or unknown are often termed dark.   Lantern lane brings back the hidden past, the forgotten past, the past that may not want to be remembered……but these are real stories....real stories that come from the streets around you.

Some of these stories may be tales of dark things.....some may simply be a charming reminder of days gone by…..regardless these stories are compelling reminders of the amazing times that precede us…..and the forgotten people of yesteryear finally get a chance to have their story told to a fresh audience.  Through you, the people of yesterday get to live again.  Will you like what you hear?

Contact Us page:-
•	A form input type page.
•	Include space for our phone number
•	Include space for our email address
Other Items:-
Social Media Links; we will be looking for social media icons to link to our social media pages to Chatterbook, Snapfolio, Chirplet.
Subscription; we want to also capture an input email address box for site visitors.  We will be launching a weekly Lantern Lane podcast / email newsetter; with a weekly Lantern Lane from a different place in the world and we want some way for people to subscribe.

Updates
Project Deadline Extended
Reason: A few additional photos have been uploaded.  Feel free to utilize if helpful.  Our stories range from the 1800s to 1950s in an era with beautiful old Victorian buildings.  I'm putting through the extension just to give some more time to see if this gives any more ideas and inspiration.  Thank you for all the great submissions.

Target Market(s)
Tourists that want to hear a darker version of the city they are visiting. Stories that other tour companies would not even think of covering. The real history of the events that ordinary people lived through that didn't necessarily make the history books. All stories are true; as per project description.
Industry/Entity Type
Tourism
Coding
Coded - Design and coding required
Number of Pages Required
5+ page
Colors
Designer to choose colors to be used in the design.
Look and feel

```html
<!DOCTYPE html>
<html lang="en">
<head>
<meta charset="utf-8">
<title>Lantern Lane Town Footpath Chronicle Trek</title>
<link href="https://fonts.googleapis.com/css2?family=Poppins:ital,wght@0,300;0,400;0,500;0,600;0,700;1,400&display=swap" rel="stylesheet">
<style>
:root{
  --red:#e5262f;
  --ink:#111111;
  --text:#8a8a8a;
  --topbar:#0b0b0b;
  --field:#3b3c40;
  --brown:#3a2a1a;
  --footer:#232323;
  --footer-deep:#1b1b1b;
  --white:#ffffff;
}
*{box-sizing:border-box;margin:0;padding:0}
html,body{width:1200px;height:2752px;overflow:hidden}
body{font-family:'Poppins',sans-serif;color:var(--ink);background:var(--white);position:relative}
.wrap{position:absolute;left:94px;width:1002px}

/* top bar */
.topbar{position:absolute;top:0;left:0;width:1200px;height:59px;background:var(--topbar);color:#ddd;font-size:13px}
.topbar .contact{position:absolute;left:94px;top:20px;display:flex;gap:30px}
.topbar .contact span{display:flex;align-items:center;gap:10px}
.topbar .right{position:absolute;right:98px;top:20px;display:flex;align-items:center;gap:22px}
.social-dot{width:9px;height:9px;border-radius:50%;background:#ddd;display:inline-block}
.topbar .account{display:flex;gap:26px;margin-left:14px}
.topbar .account span{display:flex;align-items:center;gap:8px}

/* nav */
.nav{position:absolute;top:59px;left:0;width:1200px;height:75px;background:var(--white)}
.brand{position:absolute;left:95px;top:22px;display:flex;align-items:center;gap:10px;font-size:19px;font-weight:600;color:var(--ink);letter-spacing:.5px}
.brand .mark{width:14px;height:14px;border-radius:50%;background:var(--red)}
.menu{position:absolute;left:389px;top:26px;display:flex;gap:0;font-size:13.5px;font-weight:500}
.menu a{color:var(--ink);text-decoration:none;position:relative;height:49px}
.menu a.active{color:var(--red)}
.menu a.active::after{content:"";position:absolute;left:-3px;right:-3px;bottom:0;height:3px;background:#5b8ed6}

/* hero */
.hero{position:absolute;top:134px;left:0;width:1200px;height:496px;background:linear-gradient(180deg,#7d6f8c 0%,#5c4f70 30%,#3b3046 55%,#6b5a78 70%,#2c2535 100%)}
.hero-title{position:absolute;left:137px;top:362px;font-size:48px;font-weight:600;color:#fff;line-height:1}
.hero-sub{position:absolute;left:137px;top:436px;font-size:44px;font-weight:600;color:#b9d0f0;line-height:1}
.hero-places{position:absolute;left:137px;top:494px;font-size:16px;color:#eee}
.hero-btn{position:absolute;left:137px;top:540px;width:206px;height:46px;background:var(--red);color:#fff;font-size:11.5px;font-weight:700;display:flex;align-items:center;justify-content:center;text-transform:uppercase}
.dots{position:absolute;left:577px;top:593px;display:flex;gap:6px;align-items:center}
.dots i{width:14px;height:14px;border-radius:50%;border:2px solid #ddd;display:block}
.dots i+i{width:11px;height:11px;border:none;background:#bbb}

/* quote band */
.quote-band{position:absolute;top:630px;left:0;width:1200px;height:146px;background:var(--red);color:#fff}
.quote-band .qmark{position:absolute;left:92px;top:50px;font-size:56px;font-weight:700;font-style:italic;line-height:1}
.quote-band p{position:absolute;left:150px;top:44px;width:940px;font-size:17px;font-style:italic;line-height:29px}

/* about */
.about h2{position:absolute;left:94px;top:848px;font-size:18.5px;font-weight:700;letter-spacing:.4px}
.about p{position:absolute;left:94px;width:652px;font-size:13px;line-height:24px;color:var(--text);font-weight:300}
.pill{position:absolute;left:94px;top:1136px;width:137px;height:45px;border-radius:23px;background:var(--red);color:#fff;font-size:11px;font-weight:700;display:flex;align-items:center;justify-content:center;text-transform:uppercase}
.finder{position:absolute;left:784px;top:850px;width:308px}
.finder label{display:block;font-size:12px;font-weight:600;margin-bottom:10px}
.field{height:42px;background:var(--field);color:#999;font-size:11px;display:flex;align-items:center;justify-content:space-between;padding:0 14px;margin-bottom:33px}
.finder .search{height:42px;background:var(--red);color:#fff;font-size:11px;font-weight:600;display:flex;align-items:center;justify-content:center;margin-top:-5px}

/* popular */
.popular{position:absolute;top:1279px;left:0;width:1200px;height:532px;background:radial-gradient(ellipse at 50% 40%,#4a3620 0%,#33240f 70%,#2a1e10 100%)}
.popular h2{position:absolute;left:94px;top:80px;font-size:28px;font-weight:400;color:#fff}
.cards{position:absolute;left:94px;top:163px;display:flex;gap:38px}
.card{width:222px;color:#fff}
.card .photo{height:160px}
.card h3{font-size:13.5px;font-weight:600;margin-top:26px}
.card .rating{font-size:11px;color:#aaa;margin-top:8px;display:flex;gap:6px;align-items:center}
.card .stars{color:#e0a01d;letter-spacing:1px;font-size:12px}

/* stories */
.stories h2{position:absolute;left:126px;top:1869px;font-size:22px;font-weight:400;display:flex;align-items:center}
.stories .pin{position:absolute;left:94px;top:1875px}
.stories .all{position:absolute;right:106px;top:1878px;font-size:13.5px;font-style:italic;color:var(--red)}
.story-row{position:absolute;left:94px;top:1938px;display:flex;gap:38px}
.story-row .photo{width:222px;height:209px}

/* footer */
.footer{position:absolute;top:2206px;left:0;width:1200px;height:458px;background:var(--footer);color:#aaa}
.footer .brand-f{position:absolute;left:104px;top:64px;display:flex;align-items:center;gap:10px;color:#fff;font-size:17px;font-weight:600}
.footer .brand-f i{width:70px;height:70px;border-radius:50%;background:var(--red);display:block}
.footer .about-h{position:absolute;left:102px;top:148px;font-size:32px;font-weight:700;color:#3b3b3b}
.footer .about-t{position:absolute;left:102px;top:210px;width:300px;font-size:13px;line-height:22px;color:#aaa}
.col-line{position:absolute;top:65px;width:1px;height:280px;background:#303030}
.footer h4{position:absolute;font-size:12px;font-weight:600;color:#fff;letter-spacing:1px}
.recent{position:absolute;left:448px;top:110px;width:300px}
.recent .item{display:flex;gap:20px;height:101px;border-bottom:1px solid #333;margin-bottom:0}
.recent .item+.item{padding-top:0}
.recent .thumb{width:60px;height:60px;margin-top:0}
.recent .item span{font-size:13px;font-weight:600;color:#fff;margin-top:0}
.info{position:absolute;left:793px;width:300px;font-size:12.5px;color:#aaa}
.info-social{position:absolute;left:793px;top:2464px;display:flex;gap:24px}
.info-social i{width:12px;height:12px;border-radius:50%;background:#ddd;display:block}
.copyright{position:absolute;top:2664px;left:0;width:1200px;height:88px;background:var(--footer-deep);color:#6a6a6a;font-size:13px;display:flex;align-items:center;justify-content:center}
</style>
</head>
<body>

<header class="topbar">
  <div class="contact">
    <span><svg width="13" height="13" viewBox="0 0 24 24"><path fill="#ddd" d="M6.6 10.8a15 15 0 0 0 6.6 6.6l2.2-2.2c.3-.3.7-.4 1-.2 1.1.4 2.3.6 3.6.6.6 0 1 .4 1 1V20c0 .6-.4 1-1 1C10.6 21 3 13.4 3 4c0-.6.4-1 1-1h3.5c.6 0 1 .4 1 1 0 1.3.2 2.5.6 3.6.1.3 0 .7-.2 1z"/></svg>1.98.765432</span>
    <span><svg width="15" height="12" viewBox="0 0 24 18"><rect x="1" y="1" width="22" height="16" fill="none" stroke="#ddd" stroke-width="2"/><path d="M1 1l11 9 11-9" fill="none" stroke="#ddd" stroke-width="2"/></svg>hello@lanternlanewalks.com</span>
  </div>
  <div class="right">
    <i class="social-dot"></i><i class="social-dot"></i><i class="social-dot"></i><i class="social-dot"></i>
    <div class="account">
      <span><svg width="11" height="13" viewBox="0 0 22 26"><rect x="2" y="11" width="18" height="14" fill="#ddd"/><path d="M6 11V7a5 5 0 0 1 10 0v4" fill="none" stroke="#ddd" stroke-width="3"/></svg>Login</span>
      <span><svg width="11" height="12" viewBox="0 0 22 24"><circle cx="11" cy="6" r="6" fill="#ddd"/><path d="M0 24c0-7 5-10 11-10s11 3 11 10z" fill="#ddd"/></svg>Sign Up</span>
    </div>
  </div>
</header>

<nav class="nav">
  <div class="brand"><i class="mark"></i>Lantern Lane</div>
  <div class="menu">
    <a class="active" style="margin-right:52px">Home</a>
    <a style="margin-right:49px">About Us</a>
    <a style="margin-right:49px">Book Now</a>
    <a style="margin-right:49px">Private Fucntions</a>
    <a style="margin-right:49px">All Tours</a>
    <a style="margin-right:49px">Faq</a>
    <a>Contact Us</a>
  </div>
</nav>

<section class="hero" role="img" aria-label="City skyline at dusk reflected in a river"></section>
<div class="hero-title">Dark City Tour</div>
<div class="hero-sub">3 Days in Sydney</div>
<div class="hero-places">Bern, Lucern, Zurich, Zermatt, Metahorn, Jungfrau</div>
<div class="hero-btn">Read More Lantern Lane</div>
<div class="dots"><i></i><i></i></div>

<section class="quote-band">
  <div class="qmark">“</div>
  <p>There were bits of spines, bits of skulls, &amp; finger bones spilled out all over the streets – I ended up filling three boxes. Children were playing with them for weeks</p>
</section>

<section class="about">
  <h2>ABOUT CITY HISTORICAL WALKING TOUR COMPANY</h2>
  <p style="top:896px">Dark; a euphemism for the unknown or the forgotten. Think dark ages, dark matter, dark energy; things where knowledge is uncertain or unknown are often termed dark. Lantern lane brings back the hidden past, the forgotten past, the past that may not want to be remembered……but these are real stories....real stories that come from the streets around you.</p>
  <p style="top:1000px">Some of these stories may be tales of dark things.....some may simply be a charming reminder of days gone by…..regardless these stories are compelling reminders of the amazing times that precede us…..and the forgotten people of yesteryear finally get a chance to have their story told to a fresh audience. Through you, the people of yesterday get to live again. Will you like what you hear?</p>
  <div class="pill">Learn More</div>

  <form class="finder">
    <label>Keywords</label>
    <div class="field"><span></span><svg width="12" height="12" viewBox="0 0 24 24"><circle cx="10" cy="10" r="7" fill="none" stroke="#fff" stroke-width="3"/><path d="M15 15l7 7" stroke="#fff" stroke-width="3"/></svg></div>
    <label>Duration</label>
    <div class="field"><span>Any</span><svg width="10" height="6" viewBox="0 0 10 6"><path d="M0 0h10L5 6z" fill="#fff"/></svg></div>
    <label>Date</label>
    <div class="field"><span style="color:#777">Any</span><svg width="11" height="12" viewBox="0 0 22 24"><rect x="1" y="3" width="20" height="20" fill="none" stroke="#999" stroke-width="2"/><path d="M1 9h20M6 0v5M16 0v5" stroke="#999" stroke-width="2"/></svg></div>
    <div class="search">SEARCH</div>
  </form>
</section>

<section class="popular" role="img" aria-label="Sepia photo of a Victorian arcade street as background">
  <h2>Popular Tour Packages</h2>
  <div class="cards">
    <div class="card"><div class="photo" role="img" aria-label="Rooftops of old town buildings" style="background:linear-gradient(180deg,#5a7fb8,#7c6a5c 60%,#3d3a36)"></div><h3>Tour4</h3><div class="rating"><span class="stars">☆☆☆☆☆</span>(0 Review)</div></div>
    <div class="card"><div class="photo" role="img" aria-label="Steel bridge over a river with city towers" style="background:linear-gradient(180deg,#3f7fd6,#8fb6de 55%,#3f5d6a)"></div><h3>Tour3</h3><div class="rating"><span class="stars">☆☆☆☆☆</span>(0 Review)</div></div>
    <div class="card"><div class="photo" role="img" aria-label="Clock tower with palm trees" style="background:linear-gradient(180deg,#2a6fd0,#6a8f6a 60%,#3a5a2a)"></div><h3>Tour2</h3><div class="rating"><span class="stars">☆☆☆☆☆</span>(0 Review)</div></div>
    <div class="card"><div class="photo" role="img" aria-label="Red brick Victorian building" style="background:linear-gradient(180deg,#4a86d8,#9a4a36 55%,#6a3a2a)"></div><h3>Tour1</h3><div class="rating"><span class="stars">☆☆☆☆☆</span>(0 Review)</div></div>
  </div>
</section>

<section class="stories">
  <svg class="pin" width="16" height="20" viewBox="0 0 16 20"><circle cx="8" cy="7" r="6" fill="none" stroke="#e5262f" stroke-width="2"/><path d="M5 15h6M6 18h4" stroke="#e5262f" stroke-width="2"/></svg>
  <h2>Lantern Lane</h2>
  <div class="all">/ &nbsp;Read All Articles</div>
  <div class="story-row">
    <div class="photo" role="img" aria-label="Old black and white street with a tram" style="background:linear-gradient(180deg,#d8d8d8,#8a8a8a 60%,#555)"></div>
    <div class="photo" role="img" aria-label="Old crowded street with horse carriages" style="background:linear-gradient(180deg,#c4c4c4,#7a7a7a 60%,#4a4a4a)"></div>
    <div class="photo" role="img" aria-label="Sepia city street with trams" style="background:linear-gradient(180deg,#c9b89c,#7a6a52 60%,#4a3c2c)"></div>
    <div class="photo" role="img" aria-label="Faded archival photograph of an open field" style="background:linear-gradient(180deg,#bfb6a8,#8e8578)"></div>
  </div>
</section>

<footer class="footer">
  <div class="brand-f"><i></i></div>
  <div class="about-h">About Us</div>
  <p class="about-t">Dark; a euphemism for the unknown or the forgotten. Think dark ages, dark matter, dark energy; things where knowledge is uncertain or unknown are often termed dark. Lantern lane brings back the hidden past, the forgotten past, the past that may not want to be remembered……but these are real stories...real stories that come from the streets around you.</p>
  <div class="col-line" style="left:420px"></div>
  <div class="col-line" style="left:770px"></div>

  <h4 style="left:448px;top:70px">RECENT TOURS</h4>
  <div class="recent">
    <div class="item"><div class="thumb" role="img" aria-label="Tour thumbnail of old buildings" style="background:linear-gradient(#5a7fb8,#6a5a4c)"></div><span>Tour4</span></div>
    <div class="item" style="padding-top:0"><div class="thumb" role="img" aria-label="Tour thumbnail of river bridge" style="background:linear-gradient(#3f7fd6,#4f6d7a)"></div><span>Tour3</span></div>
    <div class="item" style="border:none"><div class="thumb" role="img" aria-label="Tour thumbnail of clock tower" style="background:linear-gradient(#2a6fd0,#5a4a2a)"></div><span>Tour2</span></div>
  </div>

  <h4 style="left:793px;top:70px">CONTACT INFO</h4>
  <div class="info" style="top:115px">Address : 48 Ashgrove Row, Eastmere</div>
  <div class="info" style="top:164px">Phone : +14 5550 1184</div>
  <div class="info" style="top:195px">contact@lanternlanewalks.com</div>
</footer>
<div class="info-social"><i></i><i></i><i></i><i></i><i></i></div>

<div class="copyright">Copyright 2017 Lantern Lane Walks, All Right Reserved</div>

</body>
</html>
```